I need a bushiness card designed for my business Kind Sparrow Club attached is the logo
On the business cards I would like the following info
427 Hollister Ln #3085
Spring Tx, 77519
936-481-5527
Please free free to be creative, our business targets girls 6-11 years old, a hip and cool looking card is what we are looking for to be passed out at a girls event.......Thanks

```html
<!DOCTYPE html>
<html lang="en">
<head>
<meta charset="utf-8">
<title>Kind Sparrow Club – Business Card</title>
<link href="https://fonts.googleapis.com/css2?family=Arvo:wght@400;700&display=swap" rel="stylesheet">
<style>
  :root {
    --backdrop: #e6e7e9;
    --front-blue: #92d4e4;
    --back-teal: #1f9cc0;
    --magenta: #d4137a;
    --purple: #6e2f8c;
    --icon-violet: #7b5aa6;
    --white: #ffffff;
  }
  * { margin: 0; padding: 0; box-sizing: border-box; }
  html, body { width: 1200px; height: 1015px; overflow: hidden; }
  body {
    background: var(--backdrop);
    font-family: "Arvo", "Rockwell", serif;
    position: relative;
  }
  .card {
    position: absolute;
    left: 190px;
    width: 820px;
    height: 468px;
    border-radius: 4px;
    overflow: hidden;
    box-shadow: 0 4px 14px rgba(0,0,0,0.12);
  }
  .card--front { top: 26px; background: var(--front-blue); }
  .card--back { top: 521px; background: var(--back-teal); }

  .brand {
    position: absolute;
    left: 0; right: 0; top: 0; bottom: 0;
    display: flex;
    align-items: center;
    justify-content: center;
    gap: 22px;
  }
  .brand__dot {
    width: 46px; height: 46px;
    border-radius: 50%;
    background: var(--magenta);
  }
  .brand__name {
    font-weight: 700;
    font-size: 64px;
    color: var(--purple);
    letter-spacing: 0.5px;
  }

  .accent-block {
    position: absolute;
    left: 50px; top: 56px;
    width: 100px; height: 138px;
    background: var(--purple);
  }
  .contact-panel {
    position: absolute;
    left: 112px; top: 70px;
    width: 620px; height: 206px;
    background: var(--magenta);
    clip-path: polygon(7% 0, 100% 0, 100% 100%, 0 100%);
    padding: 30px 0 0 112px;
    color: var(--white);
    font-weight: 700;
    font-size: 33px;
    line-height: 1.3;
  }
  .links {
    position: absolute;
    left: 62px; top: 314px;
    list-style: none;
  }
  .links li {
    display: flex;
    align-items: center;
    gap: 18px;
    height: 64px;
    color: var(--white);
    font-weight: 700;
    font-size: 27px;
  }
  .links__icon {
    width: 30px; height: 30px;
    border-radius: 50%;
    background: var(--icon-violet);
    flex: none;
  }
</style>
</head>
<body>
  <section class="card card--front" aria-label="Card front">
    <div class="brand">
      <span class="brand__dot"></span>
      <span class="brand__name">Kind Sparrow Club</span>
    </div>
  </section>

  <section class="card card--back" aria-label="Card back">
    <div class="accent-block"></div>
    <address class="contact-panel">
      427 Hollister Ln #3085<br>
      Spring Tx, 77519<br>
      936-481-5527
    </address>
    <ul class="links">
      <li><span class="links__icon"></span>www.kindsparrowclub.net</li>
      <li><span class="links__icon"></span>www.friendspage.com/kindsparrowclub</li>
    </ul>
  </section>
</body>
</html>
```